BRIGHTWAY MOTOR DEALS
BRIGHTWAY MOTOR DEALS -
Creative Brief
Professional
DEAN VARLOW
SALES REP
742 N.CORVAL AVE HAMILTON OHIO 45019
BRIGHTWAYMOTORDEALS@QUILLMAIL.EXAMPLE
WWW.TORVENCARHOUSE.EXAMPLE

```html
<!DOCTYPE html>
<html lang="en">
<head>
<meta charset="utf-8">
<title>Brightway Motor Deals – Business Card</title>
<link href="https://fonts.googleapis.com/css2?family=Open+Sans:wght@400;600;700;800&display=swap" rel="stylesheet">
<style>
  :root {
    --backdrop: #3a3a3c;
    --magenta-deep: #a8127a;
    --magenta: #c2288f;
    --magenta-light: #dd5bb0;
    --card-white: #ffffff;
    --accent-green: #4dbb3c;
    --logo-ink: #c2288f;
    --text-light: #ffffff;
    --text-soft: #fbe3f2;
  }
  * { margin: 0; padding: 0; box-sizing: border-box; }
  html, body {
    width: 1200px; height: 780px; overflow: hidden;
    background: var(--backdrop);
    font-family: "Open Sans", Arial, sans-serif;
  }
  .card {
    position: absolute; left: 75px; top: 90px;
    width: 1050px; height: 600px;
    border-radius: 36px; overflow: hidden;
    display: flex;
    background: var(--card-white);
    box-shadow: 0 10px 30px rgba(0,0,0,.35);
  }
  .card-front {
    width: 440px; height: 100%;
    background: radial-gradient(ellipse at 15% 25%, var(--magenta-light) 0%, var(--magenta) 45%, var(--magenta-deep) 100%);
    color: var(--text-light);
    padding: 110px 0 0 44px;
    position: relative;
  }
  .divider {
    width: 14px; height: 100%;
    background: linear-gradient(to right, var(--card-white) 0 8px, var(--accent-green) 8px 12px, var(--card-white) 12px);
  }
  .rep-name { font-size: 42px; font-weight: 700; line-height: 1.1; }
  .rep-title { font-size: 21px; font-weight: 600; margin-top: 4px; }
  .address { font-size: 21px; line-height: 1.4; margin-top: 100px; color: var(--text-soft); }
  .contacts { list-style: none; margin-top: 40px; }
  .contacts li {
    display: flex; align-items: center; gap: 12px;
    font-size: 18px; line-height: 1; margin-bottom: 14px; color: var(--text-soft);
  }
  .contacts svg { width: 20px; height: 20px; flex: none; }
  .card-brand {
    flex: 1; position: relative;
    display: flex; flex-direction: column; align-items: center; justify-content: center;
  }
  .brand-mark {
    width: 46px; height: 46px; border-radius: 50%;
    background: var(--logo-ink); margin-bottom: 22px;
  }
  .brand-name {
    font-size: 44px; font-weight: 800; color: var(--logo-ink);
    letter-spacing: 1px; text-align: center; line-height: 1.15;
  }
</style>
</head>
<body>
  <article class="card">
    <section class="card-front">
      <h1 class="rep-name">Dean Varlow</h1>
      <p class="rep-title">Sales rep</p>
      <p class="address">742 N.Corval Ave<br>Hamilton Ohio 45019</p>
      <ul class="contacts">
        <li>
          <svg viewBox="0 0 20 20" aria-hidden="true"><circle cx="10" cy="10" r="9" fill="none" stroke="#fff" stroke-width="1.5"/><path d="M6.5 5.5l2 0 1 2.5-1.3 1a6 6 0 0 0 2.8 2.8l1-1.3 2.5 1 0 2a1 1 0 0 1-1 1A8 8 0 0 1 5.5 6.5a1 1 0 0 1 1-1z" fill="#fff"/></svg>
          513-555-0170
        </li>
        <li>
          <svg viewBox="0 0 20 20" aria-hidden="true"><rect x="6" y="2" width="8" height="16" rx="1.5" fill="#fff"/><rect x="7.3" y="4" width="5.4" height="10" fill="#c2288f"/><circle cx="10" cy="16" r=".9" fill="#c2288f"/></svg>
          513-555-0148
        </li>
        <li>
          <svg viewBox="0 0 20 20" aria-hidden="true"><circle cx="10" cy="10" r="9" fill="#fff"/><text x="10" y="14" text-anchor="middle" font-size="12" font-weight="700" fill="#c2288f" font-family="Open Sans, sans-serif">@</text></svg>
          brightwaymotordeals@quillmail.example
        </li>
        <li>
          <svg viewBox="0 0 20 20" aria-hidden="true"><circle cx="10" cy="10" r="8.5" fill="none" stroke="#fff" stroke-width="1.5"/><ellipse cx="10" cy="10" rx="3.5" ry="8.5" fill="none" stroke="#fff" stroke-width="1.2"/><path d="M1.5 10h17M3 6h14M3 14h14" stroke="#fff" stroke-width="1"/></svg>
          www.torvencarhouse.example
        </li>
      </ul>
    </section>
    <div class="divider"></div>
    <section class="card-brand">
      <div class="brand-mark"></div>
      <p class="brand-name">BRIGHTWAY<br>MOTOR DEALS</p>
    </section>
  </article>
</body>
</html>
```